Fired Up, Opt-in Focused,Wordpress Page: Bold Pulse

Here's the horrible page I just put up to share the info - BUT! it needs help majorly!!! www.boldpulse.me
I have a logo - you can work with it - or something new - this is a new site/business.
It's a fitness inspiration/makeover program.
I am part of the brand (see renaquist.com)
I can send more pics to work with.

Reason: Looking for a great site like:http://www.doratevenson.com/fit/

Target Market(s)

https://www.facebook.com/RenaQuistFitness - see my fans.

Industry/Entity Type

Fitness

Requirements
Must have
• Large opt-in box to my program at the top. Love Love Love http://www.hollybrandtner.com

Simple - easy to keep in wordpress. Not too much clutter. Easy design elements so I'm not dependant on a graphic designer for every graphic posting etc...

```html
<!DOCTYPE html>
<html lang="en">
<head>
<meta charset="utf-8">
<title>Bold Pulse – Get Fit, Be Happy</title>
<link href="https://fonts.googleapis.com/css2?family=Arvo:wght@400;700&family=Arimo:wght@400;700&display=swap" rel="stylesheet">
<style>
:root{
  --dark:#333333;
  --panel:#3e3e3e;
  --coral:#ef6a6a;
  --lilac:#9d90b4;
  --lilac-dark:#8a7da3;
  --white:#ffffff;
  --ink:#555555;
  --heading:#7a7a7a;
  --footer-text:#9a9a9a;
  --footer-bottom:#3b3b3b;
}
*{margin:0;padding:0;box-sizing:border-box}
html,body{width:669px;height:1200px;overflow:hidden;background:var(--white)}
body{position:relative;font-family:Arimo,Arial,sans-serif;color:var(--ink)}
.abs{position:absolute}

/* header */
.site-header{left:0;top:0;width:669px;height:78px;background:var(--dark)}
.header-rule{left:0;top:78px;width:669px;height:3px;background:var(--coral)}
.brand-name{left:66px;top:30px;font-family:Arvo,serif;font-size:20px;font-weight:400;color:#c4c4c4;letter-spacing:.3px}
.account{left:499px;top:9px;height:17px;display:flex;font-size:6px;text-transform:uppercase}
.account span{display:block;padding:0 8px;line-height:17px;background:var(--lilac);color:var(--white)}
.account span+span{background:#8578a0}
.main-nav{left:243px;top:39px;height:21px;display:flex;align-items:center;font-family:Arvo,serif;font-size:9px;color:var(--white)}
.main-nav a{color:inherit;text-decoration:none;margin-right:22px}
.main-nav a.active{background:var(--coral);padding:0 9px;line-height:21px;margin-right:13px}

/* hero */
.hero-band{left:0;top:81px;width:669px;height:312px;background:var(--dark)}
.hero-panel{left:66px;top:100px;width:536px;height:273px;background:var(--panel)}
.hero-photo{left:66px;top:100px;width:202px;height:217px;background:linear-gradient(160deg,#6a4a3c,#3a3030 70%)}
.hero-title{left:283px;top:136px;font-family:Arvo,serif;font-weight:400;font-size:24px;color:var(--coral);letter-spacing:.3px}
.hero-sub{left:283px;top:172px;font-family:Arvo,serif;font-weight:400;font-size:15px;line-height:20px;color:#e8e8e8}
.hero-copy{left:283px;top:225px;width:283px;font-size:7.4px;line-height:12.4px;color:#d6d6d6}
.optin{left:66px;top:317px;width:536px;height:56px;background:var(--lilac)}
.optin-title{left:76px;top:327px;font-family:Arvo,serif;font-weight:700;color:var(--white);line-height:15px}
.optin-title .l1{font-size:15px;display:block}
.optin-title .l2{font-size:11px;display:block}
.field{top:335px;width:133px;height:19px;background:var(--white)}
.submit{left:538px;top:335px;width:56px;height:19px;background:var(--lilac-dark);border:1px solid #b3a8c8;color:var(--white);font-family:Arvo,serif;font-size:10px;text-align:center;line-height:17px}
.privacy{left:254px;top:360px;font-size:7px;color:#efefef}
.privacy em{font-style:normal;color:#c9bde6}
.dots{display:flex;gap:4px}
.dots i{width:6px;height:6px;border-radius:50%;background:#111}
.dots i:first-child{background:var(--coral)}

/* feature tiles */
.tile{top:410px;width:168px;height:123px}
.tile-caption{position:absolute;left:0;bottom:0;width:100%;height:28px;background:rgba(60,60,60,.85);color:var(--white);font-family:Arvo,serif;font-weight:700;font-size:9.5px;text-align:center;line-height:28px}
.divider{left:16px;width:637px;height:10px;border-radius:50%;background:radial-gradient(ellipse at center,rgba(0,0,0,.16),rgba(0,0,0,0) 70%)}
.section-title{font-family:Arvo,serif;font-weight:400;font-size:13px;color:var(--heading)}

/* about */
.about-photo{left:66px;top:607px;width:122px;height:121px;background:linear-gradient(150deg,#8a6a5a,#2a2a2a)}
.about-copy{left:194px;top:606px;width:224px;font-size:6.2px;line-height:8.6px;color:#444;text-align:justify}
.about-copy p{margin-bottom:8px}
.video{left:430px;top:606px;width:172px;height:122px;background:linear-gradient(180deg,#6f8894,#8aa0aa 60%,#6c8591)}
.video-title{left:447px;top:652px;font-size:10px;color:#dfe7ea}
.video-bar{left:430px;top:718px;width:172px;height:10px;background:#1b1b1b}

/* results */
.results-main{left:66px;top:808px;width:262px;height:150px;background:linear-gradient(90deg,#5f6a4c 0,#7d8c63 50%,#b8743c 50%,#8e4e26)}
.thumb{top:971px;width:56px;height:55px;background:linear-gradient(90deg,#cfc8c6,#8f7b70)}

/* blog */
.post-img{left:340px;width:78px;height:77px;background:linear-gradient(160deg,#d9d2c8,#9b8a78)}
.post-title{left:423px;font-size:7px;color:var(--coral)}
.post-date{left:423px;font-size:5.6px;color:#666}
.post-body{left:423px;width:180px;font-size:6.3px;line-height:8.8px;color:#555;text-align:justify}
.read-more{left:423px;font-size:5.6px;color:var(--coral)}
.post-meta{left:340px;width:263px;height:16px;border-top:2px solid #e6e6e6;border-bottom:1px solid #e6e6e6;font-size:5px;color:#888;line-height:13px;padding-left:1px}
.share{right:2px;top:2px;display:flex;gap:2px;font-size:4.6px;line-height:8px}
.share span{padding:0 3px;border:1px solid #ccd;background:#eef1f7;color:#35508a}
.share span.n{background:#fff;color:#444;border-color:#ddd}
.share span.s{background:#e2694f;color:#fff;border-color:#e2694f}

/* footer */
.site-footer{left:0;top:1050px;width:669px;height:118px;background:var(--dark)}
.footer-col{top:1063px;font-size:6.4px;line-height:16.8px;color:var(--footer-text);list-style:none}
.social{left:502px;top:1062px;list-style:none;font-size:6.4px;color:var(--footer-text)}
.social li{display:flex;align-items:center;height:19px}
.social i{display:block;width:15px;height:15px;border-radius:50%;margin-right:9px}
.footer-bottom{left:0;top:1168px;width:669px;height:32px;background:var(--footer-bottom);text-align:center;font-size:6.4px;line-height:32px;color:#999}
</style>
</head>
<body>

<header class="abs site-header"></header>
<div class="abs header-rule"></div>
<div class="abs brand-name">Bold Pulse</div>
<div class="abs account"><span>Sign in</span><span>Register now</span></div>
<nav class="abs main-nav">
  <a class="active" href="#">HOME</a><a href="#">BLOG</a><a href="#">CONNECT</a><a href="#">FREE PERSONAL TRAINING</a><a href="#">MEET RENA</a>
</nav>

<section class="abs hero-band"></section>
<div class="abs hero-panel"></div>
<div class="abs hero-photo" role="img" aria-label="Portrait of Rena, arms crossed, smiling"></div>
<h1 class="abs hero-title">GET FIT, BE HAPPY</h1>
<h2 class="abs hero-sub">FITNESS MOTIVATION MADE EASY.<br>LIFE MADE BETTER.</h2>
<p class="abs hero-copy">The 7-Day "Bold Pulse Makeover" mini program will show you: 10 fitness mindsets that will set you for life The 2-step "get-off-the-couch process" you'll actually use The top 3 Fit For Life strategies ...and how to schedule it, do it, and always stay on track!</p>
<div class="abs optin"></div>
<div class="abs optin-title"><span class="l1">START YOUR 7-DAY</span><span class="l2">FITNESS MAKEOVER NOW!</span></div>
<div class="abs field" style="left:254px"></div>
<div class="abs field" style="left:395px"></div>
<div class="abs submit">SUBMIT</div>
<p class="abs privacy">We respect your <em>email privacy</em></p>
<div class="abs dots" style="left:570px;top:382px"><i></i><i></i><i></i></div>

<div class="abs tile" style="left:66px;background:linear-gradient(150deg,#8ea0b4,#d8d0cc)" role="img" aria-label="Woman training on a gym machine"><div class="tile-caption">BEST WORKOUT</div></div>
<div class="abs tile" style="left:250px;background:linear-gradient(150deg,#e0a070,#b8463a 60%,#6c6c8c)" role="img" aria-label="Two women doing push-ups"><div class="tile-caption">BEST FITNESS TRACKING</div></div>
<div class="abs tile" style="left:434px;background:linear-gradient(180deg,#9fb069,#5f8a3a)" role="img" aria-label="Woman stretching on a lawn outdoors"><div class="tile-caption">WORKOUT OUTSIDE</div></div>

<div class="abs divider" style="top:551px"></div>

<h3 class="abs section-title" style="left:66px;top:577px">About Rena</h3>
<div class="abs about-photo" role="img" aria-label="Rena with her four children"></div>
<div class="abs about-copy">
  <p>Rena is a self proclaimed Optimist.</p>
  <p>-a devoted wife and mom of 4 Beautiful Children ages 6, 8, 10 &amp; 12.</p>
  <p>-an entrepreneur (through and through – if you ask my husband). I've started 3+ online e-commerce business, bought and sold a successful spa, started a Green &amp; Conscious construction company with my husband – that's still running great!) and I've got a lot more projects to complete!</p>
  <p>-a life-long learner.</p>
  <p>I love being enthusiastic and motivating people to reach their potential, feel great and let go of limitations. Would love to connect with you! Send a line and share your story...</p>
</div>
<h3 class="abs section-title" style="left:430px;top:577px">Latest Video</h3>
<div class="abs video" role="img" aria-label="Video still with a cloudy sky"></div>
<div class="abs video-title">My 21-Day Total Reset Results</div>
<svg class="abs" style="left:505px;top:653px" width="20" height="20" viewBox="0 0 20 20"><rect width="20" height="20" fill="#222"/><path d="M7 5l8 5-8 5z" fill="#fff"/></svg>
<div class="abs video-bar"></div>
<div class="abs" style="left:455px;top:720px;font-size:4px;color:#aaa">0:00 / 1:02</div>

<div class="abs divider" style="top:751px"></div>

<h3 class="abs section-title" style="left:66px;top:782px">Workout Results</h3>
<div class="abs results-main" role="img" aria-label="Before and after photos of a woman's fitness results"></div>
<div class="abs thumb" style="left:70px;background:linear-gradient(90deg,#e7c7c9,#d96aa0)" role="img" aria-label="Before and after swimsuit results"></div>
<div class="abs thumb" style="left:135px" role="img" aria-label="Before and after results outdoors"></div>
<div class="abs thumb" style="left:202px;background:linear-gradient(90deg,#c98a88,#6a5050)" role="img" aria-label="Before and after results in bikini"></div>
<div class="abs thumb" style="left:270px;background:linear-gradient(90deg,#e2e2e2,#8a8a8a)" role="img" aria-label="Day 1 and day 90 comparison"></div>

<h3 class="abs section-title" style="left:339px;top:782px">Recent Blog</h3>
<div class="abs dots" style="left:570px;top:787px"><i></i><i></i><i></i></div>

<div class="abs post-img" style="top:809px" role="img" aria-label="Woman doing a push-up"></div>
<div class="abs post-title" style="top:807px">Lorem ipsum dolor sit amet, consectetur adipisicing elit,</div>
<div class="abs post-date" style="top:818px">05 April 2013</div>
<p class="abs post-body" style="top:829px">ed do eiusmod tempor incididunt ut labore et dolore magna aliqua. Ut enim ad minim veniam, quis nostrud exercitation ullamco laboris nisi ut aliquip ex ea commodo consequat. Duis aute irure dolor in reprehenderit in voluptate velit esse cillum dolore eu fugiat nulla pariatur.</p>
<div class="abs read-more" style="top:878px">READ MORE</div>
<div class="abs post-meta" style="top:893px">Posted by: Rena<div class="abs share"><span>Like</span><span class="n">26</span><span>Post</span><span class="n">97</span><span class="s">Share</span><span class="n">832</span></div></div>

<div class="abs post-img" style="top:920px" role="img" aria-label="Woman doing a push-up"></div>
<div class="abs post-title" style="top:919px">Lorem ipsum dolor sit amet, consectetur adipisicing elit,</div>
<div class="abs post-date" style="top:930px">05 April 2013</div>
<p class="abs post-body" style="top:941px">ed do eiusmod tempor incididunt ut labore et dolore magna aliqua. Ut enim ad minim veniam, quis nostrud exercitation ullamco laboris nisi ut aliquip ex ea commodo consequat. Duis aute irure dolor in reprehenderit in voluptate velit esse cillum dolore eu fugiat nulla pariatur.</p>
<div class="abs read-more" style="top:990px">READ MORE</div>
<div class="abs post-meta" style="top:1005px">Posted by: Rena<div class="abs share"><span>Like</span><span class="n">26</span><span>Post</span><span class="n">97</span><span class="s">Share</span><span class="n">832</span></div></div>

<footer class="abs site-footer"></footer>
<ul class="abs footer-col" style="left:106px"><li>Blog</li><li>Connect</li><li>Free Personal Training</li><li>Meet Rena</li><li>Sitemap</li><li>Privacy Policy</li></ul>
<ul class="abs footer-col" style="left:234px"><li>The Routine</li><li>Sample Fitness Plan</li><li>The Fuel</li><li>Sample Meal Plan</li><li>The Tools</li><li>The App</li></ul>
<ul class="abs footer-col" style="left:368px"><li>Best Workouts</li><li>Workout outside</li><li>Best Fitness Tracking</li><li>Personal Fitness  training</li><li>Shoreline fitness training</li><li>Why it Works</li></ul>
<ul class="abs social">
  <li><i style="background:#3b5998"></i>Friendwall</li>
  <li><i style="background:#2ba3e1"></i>Chirper</li>
  <li><i style="background:#d9412f"></i>Circleplus</li>
  <li><i style="background:#d8332a"></i>Clipstream</li>
  <li><i style="background:#ef6a23"></i>Blog</li>
</ul>
<div class="abs footer-bottom">© 2013 Bold Pulse: Get Fit, Be Happy</div>

</body>
</html>
```